Young, dynamic furniture company needs a new business card design

We require a new business card design for our modern furniture company which supplies furniture and appliances to the property and development market.
Oakline Furnishings has become one of the leading furniture & appliance suppliers to the property market withing London. With over 10 years experience, we have increased our business to supply not only private landlords and managing agents, but also property developers, housing associations and local councils.
We offer not only a complete range of furniture which includes beds, wardrobes, dining sets and sofas, but also a high quality, full delivery and assembly service to help you with all our furnishing needs.

Target Market(s)

Private landlords, estate agents, letting agents, property management companies

Industry/Entity Type

Business

Contact Information for Business Card

Name,
Title,
Address,
Mobile,
Telephone,
Fax, Website, email address

Font styles to use
Sans Serif

Colors
3176b5
0555a3
85abd2
cfdeed

Requirements
Must have
• All the above information for each of our staff, along with our logo

```html
<!DOCTYPE html>
<html lang="en">
<head>
<meta charset="utf-8">
<title>Oakline Furnishings – Business Card</title>
<link href="https://fonts.googleapis.com/css2?family=Montserrat:wght@500;600;700&family=Open+Sans:wght@400;600&display=swap" rel="stylesheet">
<style>
  :root{
    --page:#ecebe8;
    --navy:#1d2c63;
    --navy-deep:#17244f;
    --blue:#0555a3;
    --mid-blue:#3176b5;
    --light-blue:#85abd2;
    --pale-blue:#cfdeed;
    --ink:#4a4d55;
    --rule:#8c8f96;
    --white:#ffffff;
  }
  *{box-sizing:border-box;margin:0;padding:0}
  html,body{width:1200px;height:843px;overflow:hidden;background:var(--page)}
  .sheet{position:relative;width:1200px;height:843px}

  .card{position:absolute;width:620px;height:354px;overflow:hidden;
    box-shadow:0 10px 28px rgba(0,0,0,.18)}

  /* back */
  .card--back{left:120px;top:40px;
    background:linear-gradient(135deg,#2c4290 0%,var(--navy) 55%,var(--navy-deep) 100%);
    color:var(--white);text-align:center;font-family:'Montserrat',sans-serif}
  .back-brand{position:absolute;left:0;right:0;top:128px;display:flex;justify-content:center;align-items:center;gap:14px}
  .brand-square{width:30px;height:30px;background:var(--white)}
  .back-name{font-size:30px;font-weight:600;letter-spacing:1px;text-transform:uppercase}
  .back-tagline{position:absolute;left:0;right:0;top:182px;font-size:11px;letter-spacing:3px;
    text-transform:uppercase;color:var(--pale-blue)}
  .back-web{position:absolute;left:0;right:0;top:270px;font-family:'Open Sans',sans-serif;
    font-size:14px;letter-spacing:6px;color:var(--pale-blue)}

  /* front */
  .card--front{left:460px;top:448px;background:linear-gradient(160deg,#ffffff 0%,#f1f2f4 100%);
    font-family:'Open Sans',sans-serif;color:var(--ink)}
  .holder{position:absolute;left:40px;top:70px}
  .holder-name{font-family:'Montserrat',sans-serif;font-size:22px;font-weight:700;color:var(--navy);letter-spacing:.5px}
  .holder-title{font-family:'Montserrat',sans-serif;font-size:15px;font-weight:600;color:var(--mid-blue);letter-spacing:.5px;margin-top:2px}
  .divider{position:absolute;left:40px;top:130px;width:400px;height:1px;background:var(--rule)}
  .contacts{position:absolute;left:40px;top:146px;list-style:none}
  .contacts li{display:flex;align-items:center;gap:12px;height:24px;font-size:15px;color:var(--ink)}
  .contacts svg{width:16px;height:16px;fill:var(--navy);flex:none}

  .brand{position:absolute;right:36px;top:78px;text-align:left}
  .brand-row{display:flex;align-items:center;gap:10px}
  .brand-row .brand-square{width:24px;height:24px;background:var(--blue)}
  .brand-name{font-family:'Montserrat',sans-serif;font-size:19px;font-weight:600;color:var(--navy);text-transform:uppercase;letter-spacing:.3px}
  .brand-tagline{font-family:'Montserrat',sans-serif;font-size:9.5px;font-weight:600;letter-spacing:.8px;
    color:var(--navy);text-transform:uppercase;margin:4px 0 0 34px}
  .brand-rule{position:absolute;right:36px;top:150px;width:210px;height:1px;background:var(--rule)}

  .address{position:absolute;right:36px;top:190px;text-align:right;font-size:15px;line-height:22px;color:var(--ink)}
  .address .web{letter-spacing:2.5px}

  .base-band{position:absolute;left:0;right:0;bottom:0;height:22px;
    background:linear-gradient(90deg,var(--blue),var(--navy));border-top:3px solid var(--light-blue)}
</style>
</head>
<body>
<main class="sheet">

  <section class="card card--back" aria-label="Card back">
    <div class="back-brand"><span class="brand-square"></span><span class="back-name">Oakline Furnishings</span></div>
    <p class="back-tagline">Trade Furniture Solutions</p>
    <p class="back-web">www.oakline.co</p>
  </section>

  <section class="card card--front" aria-label="Card front">
    <div class="holder">
      <h1 class="holder-name">MARTIN HALE</h1>
      <p class="holder-title">PRESIDENT</p>
    </div>
    <div class="divider"></div>
    <ul class="contacts">
      <li><svg viewBox="0 0 16 16" aria-hidden="true"><path d="M2 5c0-2 2-3 6-3s6 1 6 3v1h-3V5H5v1H2zM4 7h8l2 7H2zM8 9a2 2 0 100 4 2 2 0 000-4z"/></svg>020 7946 0318</li>
      <li><svg viewBox="0 0 16 16" aria-hidden="true"><path d="M4 1h8v14H4zM5.5 2.5v9h5v-9zM7 13h2v1H7z" fill-rule="evenodd"/></svg>07700 900 462</li>
      <li><svg viewBox="0 0 16 16" aria-hidden="true"><path d="M4 1h8v5H4zM1 6h14v7H1zM4 11h8v4H4z"/></svg>020 7946 0319</li>
      <li><svg viewBox="0 0 16 16" aria-hidden="true"><path d="M1 3h14v10H1zM1 3l7 6 7-6" stroke="#fff" stroke-width="1"/></svg>martin@oakline.co</li>
    </ul>

    <div class="brand">
      <div class="brand-row"><span class="brand-square"></span><span class="brand-name">Oakline Furnishings</span></div>
      <p class="brand-tagline">Trade Furniture Solutions</p>
    </div>
    <div class="brand-rule"></div>

    <address class="address" style="font-style:normal">
      42 Harrow Lane<br>
      London, NW6 2QR<br>
      <span class="web">www.oakline.co</span>
    </address>

    <div class="base-band"></div>
  </section>

</main>
</body>
</html>
```